Need a Zine cover designed

I’m looking for someone who can design an eye catching and original zine cover. Incorporating the logo I included below. I’m not 100% sure which logo I want to use on the cover, if it’s possible to see how you incorporate the logos on a sample will make it easier for me to decide. Thank you for your time.
For the second logo I’m unsure how to remove the grey background, but I do not want it included in the zine cover
The title of the zine is:
Amber Crossroads
perspectives of culture, life, & love

```html
<!DOCTYPE html>
<html lang="en">
<head>
<meta charset="utf-8">
<title>Amber Crossroads — Zine Cover</title>
<link rel="stylesheet" href="https://fonts.googleapis.com/css2?family=Bowlby+One&family=Permanent+Marker&display=swap">
<style>
  :root {
    --backdrop: #a3a4a7;
    --paper: #c9a497;
    --paper-light: #d3b2a6;
    --paper-dark: #b99284;
    --spine: #bd988a;
    --crease: rgba(120, 84, 72, 0.35);
    --crease-light: rgba(255, 240, 232, 0.35);
    --ink-red: #c0181c;
  }
  * { margin: 0; padding: 0; box-sizing: border-box; }
  html, body {
    width: 1176px;
    height: 1200px;
    overflow: hidden;
    background: var(--backdrop);
  }
  .stage {
    width: 1176px;
    height: 1200px;
    display: flex;
    align-items: center;
    justify-content: center;
  }
  .zine-cover {
    position: relative;
    width: 820px;
    height: 1120px;
    background: radial-gradient(ellipse at 40% 35%, var(--paper-light), var(--paper) 55%, var(--paper-dark));
    overflow: hidden;
  }
  .spine-band {
    position: absolute;
    left: 0; top: 0; bottom: 0;
    width: 46px;
    background: var(--spine);
    border-right: 1px solid var(--crease);
  }
  .fold-lines {
    position: absolute;
    inset: 0;
  }
  .brand {
    position: absolute;
    left: 190px;
    top: 160px;
    display: flex;
    align-items: center;
    gap: 14px;
    transform: rotate(-9deg);
    white-space: nowrap;
  }
  .brand-dot {
    width: 22px;
    height: 22px;
    border-radius: 50%;
    background: var(--ink-red);
  }
  .brand-name {
    font-family: "Permanent Marker", cursive;
    font-size: 38px;
    color: var(--ink-red);
    line-height: 1;
  }
  .title {
    position: absolute;
    left: 120px;
    top: 440px;
    width: 660px;
    transform: rotate(-9deg);
    transform-origin: left top;
    font-family: "Bowlby One", sans-serif;
    font-weight: 400;
    color: var(--ink-red);
    text-transform: uppercase;
    line-height: 0.98;
    white-space: nowrap;
  }
  .title-line { display: block; }
  .title-line--first { font-size: 92px; padding-left: 40px; }
  .title-line--second { font-size: 74px; }
  .tagline {
    position: absolute;
    left: 320px;
    top: 950px;
    transform: rotate(-14deg);
    transform-origin: left top;
    font-family: "Permanent Marker", cursive;
    color: var(--ink-red);
    text-transform: uppercase;
    line-height: 1.05;
    white-space: nowrap;
  }
  .tagline-top { display: block; font-size: 32px; }
  .tagline-bottom { display: block; font-size: 48px; }
</style>
</head>
<body>
  <main class="stage">
    <section class="zine-cover" aria-label="Zine cover: Amber Crossroads">
      <div class="spine-band"></div>
      <svg class="fold-lines" width="820" height="1120" viewBox="0 0 820 1120" aria-hidden="true">
        <g fill="none" stroke-width="2">
          <path d="M46 300 L820 260" stroke="var(--crease)"/>
          <path d="M46 303 L820 263" stroke="var(--crease-light)"/>
          <path d="M46 600 L820 560" stroke="var(--crease)"/>
          <path d="M46 603 L820 563" stroke="var(--crease-light)"/>
          <path d="M46 880 L820 840" stroke="var(--crease)"/>
          <path d="M46 883 L820 843" stroke="var(--crease-light)"/>
          <path d="M420 0 L445 1120" stroke="var(--crease)"/>
          <path d="M423 0 L448 1120" stroke="var(--crease-light)"/>
        </g>
      </svg>

      <div class="brand">
        <span class="brand-dot"></span>
        <span class="brand-name">Sunday Drifters Club</span>
      </div>

      <h1 class="title">
        <span class="title-line title-line--first">Amber</span>
        <span class="title-line title-line--second">Crossroads</span>
      </h1>

      <p class="tagline">
        <span class="tagline-top">Perspectives of life</span>
        <span class="tagline-bottom">Culture &amp; Love</span>
      </p>
    </section>
  </main>
</body>
</html>
```